Medical Services Banner Set Project - revised

We need 3 standard size banner sets for each of two medical specialties: bariatric weight loss surgery and plastic surgery.
Our preference is for 3 versions of each set.
1. Interactive flash banner
2. Animated flash banner
3. Static banner
The theme is transition from ugly to beautiful and from fat to thin In looking at other similar banners we believe the key to proper execution is the rendering of the body transition.This is quite difficult to achieve - I have seen multiple attempts and no one can seem to get it just right (realistic and credible).
Action script for interactive banner begins with “before” image, click initiates the action script and image morphs into “after” image (beautiful/thin/sexy)
Animated is same but not interactive, transition on slow loop
Static version uses the” after” image only
Tags lines are respectively:
Stop Dieting and Start Living! (weight loss surgery)
Discover the New You! (plastic surgery)
Sizes:
300x250
728x90
160x600
Name of Company: Norden Bariatric and Talvik Cosmetic Surgery
Logo is attached - please do not use tag line

```html
<!DOCTYPE html>
<html lang="en">
<head>
<meta charset="utf-8">
<title>Norden Bariatric – Banner Set</title>
<link href="https://fonts.googleapis.com/css2?family=Cinzel:wght@400;600;700&display=swap" rel="stylesheet">
<style>
  :root{
    --blue:#1b4f96;
    --grey:#a3a0a0;
    --grey-light:#d9d8d8;
    --white:#ffffff;
    --ink:#2a2a2a;
    --skin-light:#ecc19f;
    --skin-dark:#c88a62;
    --stage-dark:#141414;
    --stage-light:#5a5a5a;
  }
  *{margin:0;padding:0;box-sizing:border-box}
  html,body{width:1200px;height:900px;overflow:hidden}
  body{
    position:relative;
    background:radial-gradient(ellipse at 30% 20%,var(--stage-light),var(--stage-dark) 80%);
    font-family:"Cinzel",serif;
  }
  .banner{position:absolute;background:var(--white);overflow:hidden;box-shadow:6px 8px 14px rgba(0,0,0,.55)}
  .banner svg.swoosh{position:absolute;left:0;top:0}
  .photo{
    position:absolute;
    background:linear-gradient(180deg,var(--white) 0%,var(--skin-light) 22%,var(--skin-dark) 70%,var(--skin-light) 100%);
  }
  .label{
    position:absolute;background:var(--grey);color:var(--white);
    border-radius:0 9px 9px 0;box-shadow:5px 6px 0 var(--blue);
    display:flex;align-items:center;justify-content:center;
    font-weight:400;letter-spacing:1px;
  }
  .footer-bar{
    position:absolute;left:0;right:0;bottom:0;background:var(--blue);color:var(--white);
    display:flex;align-items:center;justify-content:center;font-weight:400;letter-spacing:.5px;
  }
  .brand{position:absolute;display:flex;align-items:center;gap:8px}
  .brand-mark{background:var(--blue);flex:none}
  .brand-name{color:var(--blue);font-weight:400;white-space:nowrap;letter-spacing:0}

  /* square banners */
  .square{width:430px;height:356px;top:42px}
  .square.before{left:98px}
  .square.after{left:640px}
  .square .photo{left:222px;top:80px;width:175px;height:246px}
  .square .label{left:0;top:158px;width:187px;height:45px;font-size:28px}
  .square .footer-bar{height:30px;font-size:17px}
  .square.after .footer-bar{font-size:21px}
  .square .brand{left:212px;top:24px}
  .square .brand-mark{width:14px;height:14px}
  .square .brand-name{font-size:15px}

  /* leaderboard */
  .leader{left:98px;top:444px;width:1044px;height:128px}
  .leader .brand{left:22px;top:50px}
  .leader .brand-mark{width:20px;height:20px}
  .leader .brand-name{font-size:22px}
  .leader .tagline{
    position:absolute;left:365px;top:52px;width:380px;height:26px;
    background:linear-gradient(90deg,var(--grey) 0%,var(--grey-light) 60%,var(--white) 100%);
    color:var(--ink);font-size:16px;font-weight:400;
    display:flex;align-items:center;justify-content:center;
  }
  .leader .photo{left:760px;top:0;width:72px;height:128px}
  .leader .label{left:858px;top:42px;width:186px;height:48px;font-size:28px}

  /* wide before/after */
  .wide{left:98px;top:628px;width:860px;height:229px}
  .wide .brand{left:16px;top:98px}
  .wide .brand-mark{width:16px;height:16px}
  .wide .brand-name{font-size:16px}
  .wide .top-bar{
    position:absolute;left:200px;top:0;right:0;height:33px;background:var(--grey);
    color:var(--white);font-size:21px;font-weight:400;
    display:flex;align-items:center;justify-content:center;padding-left:40px;
  }
  .wide .photo{top:33px;width:106px;height:159px}
  .wide .photo.before-shot{left:424px}
  .wide .photo.after-shot{left:617px}
  .wide .label{top:95px;height:35px;font-size:22px}
  .wide .label.before{left:292px;width:128px}
  .wide .label.after{left:718px;width:142px}
  .wide .rule{position:absolute;left:345px;right:0;top:192px;height:3px;background:var(--grey)}
  .wide .closing{
    position:absolute;left:440px;top:197px;width:390px;height:30px;
    color:var(--blue);font-size:27px;font-weight:400;
    display:flex;align-items:center;justify-content:center;
  }
</style>
</head>
<body>

<section class="banner square before">
  <div class="photo" role="img" aria-label="Rear view of a woman in white top and dark bikini, before weight loss"></div>
  <svg class="swoosh" width="430" height="356" viewBox="0 0 430 356" aria-hidden="true">
    <path d="M0,30 C120,28 230,72 320,92 C380,104 412,84 430,42 L430,58 C402,112 355,124 300,116 C210,102 110,44 0,40 Z" fill="var(--blue)"/>
  </svg>
  <div class="brand">
    <div class="brand-mark"></div>
    <div class="brand-name">Norden Bariatric</div>
  </div>
  <div class="label">BEFORE</div>
  <div class="footer-bar">STOP DIETING AND START LIVING!</div>
</section>

<section class="banner square after">
  <div class="photo" role="img" aria-label="Rear view of a slimmer woman in white top and dark bikini, after weight loss"></div>
  <svg class="swoosh" width="430" height="356" viewBox="0 0 430 356" aria-hidden="true">
    <path d="M0,30 C120,28 230,72 320,92 C380,104 412,84 430,42 L430,58 C402,112 355,124 300,116 C210,102 110,44 0,40 Z" fill="var(--blue)"/>
  </svg>
  <div class="brand">
    <div class="brand-mark"></div>
    <div class="brand-name">Norden Bariatric</div>
  </div>
  <div class="label">AFTER</div>
  <div class="footer-bar">DISCOVER THE NEW YOU!</div>
</section>

<section class="banner leader">
  <svg class="swoosh" width="1044" height="128" viewBox="0 0 1044 128" aria-hidden="true">
    <path d="M288,128 C340,110 370,60 398,0 L408,0 C385,62 350,112 302,128 Z" fill="var(--blue)"/>
  </svg>
  <div class="brand">
    <div class="brand-mark"></div>
    <div class="brand-name">Norden Bariatric</div>
  </div>
  <div class="tagline">STOP DIETING AND START LIVING!</div>
  <div class="photo" role="img" aria-label="Rear view of a woman in bikini, before weight loss"></div>
  <div class="label">BEFORE</div>
</section>

<section class="banner wide">
  <svg class="swoosh" width="860" height="229" viewBox="0 0 860 229" aria-hidden="true">
    <path d="M190,0 L205,0 C240,90 300,180 400,229 L375,229 C285,185 225,100 190,0 Z" fill="var(--blue)"/>
  </svg>
  <div class="top-bar">STOP DIETING AND START LIVING!</div>
  <div class="brand">
    <div class="brand-mark"></div>
    <div class="brand-name">Norden Bariatric</div>
  </div>
  <div class="label before">BEFORE</div>
  <div class="photo before-shot" role="img" aria-label="Rear view of a woman in bikini, before weight loss"></div>
  <div class="photo after-shot" role="img" aria-label="Rear view of a slimmer woman in bikini, after weight loss"></div>
  <div class="label after">AFTER</div>
  <div class="rule"></div>
  <div class="closing">DISCOVER THE NEW YOU!</div>
</section>

</body>
</html>
```